Bay & Meadow Property Services Tri-fold sales & marketing brochure

We need a tri-fold brochure that describes our three lines of business and the various services within each line to use in sales and marketing efforts.
See website for additional background info:
https://halvernq7.example-host.com/

Target Market(s)

Real Estate Investors & owners in Residential Rental, Short-term Rentals, and Mini/Maxi Storage Rental markets

Requirements
Must have
• See attached logo, use color scheme & font styles to match. Make sure to utilize photos to enhance look/feel.

```html
<!DOCTYPE html>
<html lang="en">
<head>
<meta charset="utf-8">
<title>Bay &amp; Meadow Property Services — Tri-fold Brochure</title>
<link href="https://fonts.googleapis.com/css2?family=Libre+Baskerville:ital,wght@0,400;0,700;1,400&family=Montserrat:ital,wght@0,400;0,500;0,600;1,400&display=swap" rel="stylesheet">
<style>
:root{
  --cyan:#0aa2c9;
  --ink:#262526;
  --text:#1d1d1d;
  --muted:#6d6d6d;
  --backdrop:#9c9c9c;
  --paper:#ffffff;
  --tab-shadow:#d6d6d6;
  --serif:'Libre Baskerville',serif;
  --sans:'Montserrat',sans-serif;
}
html,body{margin:0;padding:0;width:800px;height:1200px;overflow:hidden;background:var(--backdrop);}
.spread{position:absolute;left:20px;width:760px;height:588px;background:var(--paper);overflow:hidden;}
.spread--outside{top:8px;}
.spread--inside{top:604px;}
.spread__art{position:absolute;left:0;top:0;width:760px;height:588px;}
.panel{position:absolute;top:0;width:253px;height:588px;}
.panel--left{left:0;}
.panel--middle{left:253px;width:254px;}
.panel--right{left:507px;}
.fold{position:absolute;top:0;width:14px;height:588px;background:linear-gradient(90deg,rgba(0,0,0,.07),rgba(0,0,0,0));}

/* shared type */
.tab{position:absolute;left:0;height:26px;background:var(--cyan);color:#fff;font:700 11.5px/1 var(--serif);display:flex;align-items:center;padding-left:14px;box-sizing:border-box;border-radius:0 7px 7px 0;box-shadow:3px 3px 0 var(--tab-shadow);letter-spacing:.2px;}
.blurb{position:absolute;left:16px;width:212px;margin:0;font:500 7.7px/11.2px var(--sans);color:var(--text);}

/* outside: why work with us */
.why-title{position:absolute;top:14px;left:0;width:253px;margin:0;text-align:center;color:#fff;font:700 16px/22px var(--serif);letter-spacing:.5px;}

/* outside: contact */
.brand-mark{position:absolute;display:flex;align-items:center;gap:8px;}
.brand-mark__dot{border-radius:50%;background:var(--cyan);flex:none;}
.tagline{position:absolute;top:152px;left:0;width:254px;margin:0;text-align:center;color:#fff;font:500 14px/21px var(--sans);}
.contact-title{position:absolute;top:214px;left:0;width:254px;margin:0;text-align:center;color:#fff;font:700 20px/1 var(--serif);letter-spacing:.5px;}
.icon-dot{position:absolute;left:110px;width:34px;height:34px;border-radius:50%;background:var(--cyan);display:flex;align-items:center;justify-content:center;}
.contact-phone{position:absolute;top:358px;left:0;width:254px;text-align:center;font:500 21px/1 var(--sans);color:var(--text);margin:0;}
.contact-email{position:absolute;top:437px;left:0;width:254px;text-align:center;font:500 8.6px/1 var(--sans);color:var(--text);margin:0;}
.contact-address{position:absolute;top:504px;left:0;width:254px;text-align:center;font:500 11px/16px var(--sans);color:var(--text);margin:0;font-style:normal;}

/* outside: cover */
.cover-headline{position:absolute;top:404px;left:0;width:253px;margin:0;text-align:center;color:var(--ink);font:700 19.5px/1 var(--serif);}
.cover-sub{position:absolute;top:428px;left:0;width:253px;margin:0;text-align:center;color:var(--cyan);font:700 11.6px/1 var(--serif);}
.cover-intro{position:absolute;top:446px;left:14px;width:225px;margin:0;text-align:center;color:var(--muted);font:italic 400 10.6px/16px var(--sans);}
.phone-pill{position:absolute;top:534px;left:36px;width:180px;height:26px;border-radius:6px;background:var(--cyan);color:#fff;font:500 15px/26px var(--sans);text-align:center;box-shadow:3px 3px 0 var(--tab-shadow);}

/* inside: about */
.about-kicker{position:absolute;top:88px;left:10px;margin:0;font:700 12px/15px var(--serif);color:var(--ink);}
.about-title{position:absolute;top:103px;left:10px;margin:0;font:700 12px/15px var(--serif);color:var(--cyan);}
.rule{position:absolute;left:10px;width:40px;height:3px;background:var(--cyan);}
.about-lead{position:absolute;top:152px;left:10px;margin:0;font:700 11.4px/15px var(--serif);color:var(--cyan);}
.copy{position:absolute;left:11px;width:232px;margin:0;font:500 7.9px/12.6px var(--sans);color:var(--text);}
.approach-title{position:absolute;top:403px;left:10px;margin:0;font:700 11.4px/1 var(--serif);color:var(--cyan);}

/* inside: expertise */
.section-pill{position:absolute;height:26px;background:var(--cyan);color:#fff;font:700 11.6px/26px var(--serif);text-align:center;border-radius:6px;box-shadow:3px 3px 0 var(--tab-shadow);letter-spacing:.3px;}
.expertise-icon{position:absolute;left:12px;width:28px;height:28px;}
.expertise-head{position:absolute;left:55px;width:190px;margin:0;font:700 9.6px/12.5px var(--serif);color:var(--cyan);letter-spacing:.2px;}
.expertise-copy{position:absolute;left:15px;width:225px;margin:0;font:500 7.7px/11.3px var(--sans);color:var(--text);}

/* inside: sectors */
.sector-icon{position:absolute;left:106px;width:40px;height:30px;}
.sector-label{position:absolute;left:0;width:253px;margin:0;text-align:center;font:400 8.1px/1 var(--serif);color:var(--ink);letter-spacing:.2px;}
.services-banner{position:absolute;top:268px;left:30px;width:223px;height:34px;background:var(--cyan);color:#fff;font:700 11.4px/14px var(--serif);text-align:center;display:flex;align-items:center;justify-content:center;box-shadow:-3px 3px 0 var(--tab-shadow);letter-spacing:.3px;}
</style>
</head>
<body>

<!-- ============ OUTSIDE SPREAD ============ -->
<section class="spread spread--outside">
  <svg class="spread__art" viewBox="0 0 760 588" aria-hidden="true">
    <defs>
      <linearGradient id="villaPhoto" x1="0" y1="0" x2="0" y2="1">
        <stop offset="0" stop-color="#8fb7d8"/>
        <stop offset=".35" stop-color="#d9cfc4"/>
        <stop offset=".6" stop-color="#b58a6e"/>
        <stop offset=".8" stop-color="#3fb3b0"/>
        <stop offset="1" stop-color="#6e8a3a"/>
      </linearGradient>
      <linearGradient id="keyPhoto" x1="0" y1="0" x2="1" y2="1">
        <stop offset="0" stop-color="#a9885f"/>
        <stop offset=".5" stop-color="#c9a77c"/>
        <stop offset="1" stop-color="#8b6b47"/>
      </linearGradient>
    </defs>
    <!-- left panel header band -->
    <path d="M0 0H253V34Q140 92 0 46Z" fill="#262526"/>
    <!-- left panel bottom photo -->
    <path d="M0 462C80 440 170 430 253 440V588H0Z" fill="url(#keyPhoto)" role="img" aria-label="Photo of a small model house with a red wall and a set of keys on a wooden table"/>
    <path d="M0 448C80 426 170 418 253 430V440C170 430 80 440 0 462Z" fill="#0aa2c9"/>
    <path d="M0 440C80 414 170 406 253 420V424C170 411 80 419 0 444Z" fill="#0aa2c9"/>
    <!-- middle panel dark block -->
    <path d="M253 0H507V244C450 256 390 282 330 278C300 276 270 262 253 250Z" fill="#262526"/>
    <!-- right panel photo -->
    <path d="M507 0H760V226C690 222 600 240 507 248Z" fill="url(#villaPhoto)" role="img" aria-label="Photo of a modern white villa with large windows and an infinity pool"/>
    <!-- cyan swoosh -->
    <path d="M253 256C290 292 350 306 420 292C500 275 600 242 680 228C720 222 745 224 760 228V276C735 258 700 254 650 260C570 268 500 284 430 300C360 316 290 306 253 270Z" fill="#0aa2c9"/>
    <path d="M253 248C295 286 350 296 420 283C500 267 600 232 680 220C720 214 745 216 760 220V224C745 220 720 218 680 224C600 236 500 271 420 287C350 300 295 290 253 254Z" fill="#ffffff"/>
  </svg>
  <div class="fold" style="left:253px"></div>
  <div class="fold" style="left:507px"></div>

  <!-- Left panel -->
  <div class="panel panel--left">
    <h2 class="why-title">WHY WORK<br>WITH US?</h2>

    <div class="tab" style="top:79px;width:201px">END-TO-END EXECUTION:</div>
    <p class="blurb" style="top:112px">From off-market sourcing to design, construction, management, and exit—we do it all.</p>

    <div class="tab" style="top:146px;width:201px">NICHE MARKET FOCUS:</div>
    <p class="blurb" style="top:179px">STRs and Storage are two of the fastest-growing real estate classes. We help you dominate both.</p>

    <div class="tab" style="top:213px;width:201px">PROVEN TRACK RECORD:</div>
    <p class="blurb" style="top:246px">We’ve built and managed profitable assets from scratch—and helped others do the same.</p>

    <div class="tab" style="top:280px;width:223px">SYSTEM-DRIVEN EFFICIENCY:</div>
    <p class="blurb" style="top:313px">We harness automation for pricing, bookings, leasing, and reporting so your assets work harder, not you.</p>

    <div class="tab" style="top:358px;width:201px">FLEXIBLE PARTNERSHIP:</div>
    <p class="blurb" style="top:391px">Hands-on or hands-off, we support your style of investing.</p>
  </div>

  <!-- Middle panel -->
  <div class="panel panel--middle">
    <div class="brand-mark" style="top:54px;left:0;width:254px;justify-content:center">
      <span class="brand-mark__dot" style="width:30px;height:30px"></span>
      <span style="font:700 15px/1 var(--serif);color:#fff">Bay &amp; Meadow</span>
    </div>
    <p class="tagline">Let’s build something<br>valuable—together.</p>
    <h2 class="contact-title">CONTACT US</h2>

    <div class="icon-dot" style="top:322px">
      <svg width="18" height="18" viewBox="0 0 24 24" aria-hidden="true"><path d="M6.6 10.8a15.1 15.1 0 0 0 6.6 6.6l2.2-2.2c.3-.3.7-.4 1-.2 1.1.4 2.3.6 3.6.6.6 0 1 .4 1 1V20c0 .6-.4 1-1 1A17 17 0 0 1 3 4c0-.6.4-1 1-1h3.5c.6 0 1 .4 1 1 0 1.3.2 2.5.6 3.6.1.3 0 .7-.2 1z" fill="#fff"/><path d="M15 3a6 6 0 0 1 6 6M15 6.5a2.5 2.5 0 0 1 2.5 2.5" stroke="#fff" stroke-width="1.6" fill="none" stroke-linecap="round"/></svg>
    </div>
    <p class="contact-phone">(555) 214-3860</p>

    <div class="icon-dot" style="top:398px">
      <svg width="18" height="18" viewBox="0 0 24 24" aria-hidden="true"><circle cx="12" cy="12" r="9" fill="none" stroke="#fff" stroke-width="1.6"/><ellipse cx="12" cy="12" rx="4" ry="9" fill="none" stroke="#fff" stroke-width="1.6"/><path d="M3 12h18M5 7h14M5 17h14" stroke="#fff" stroke-width="1.4"/></svg>
    </div>
    <p class="contact-email">info@baymeadowproperty.example</p>

    <div class="icon-dot" style="top:469px">
      <svg width="18" height="18" viewBox="0 0 24 24" aria-hidden="true"><path d="M12 2a7 7 0 0 0-7 7c0 5 7 13 7 13s7-8 7-13a7 7 0 0 0-7-7z" fill="#fff"/><circle cx="12" cy="9" r="2.6" fill="#0aa2c9"/></svg>
    </div>
    <address class="contact-address">Bay &amp; Meadow Property Services<br>412 Willowbrook Lane<br>Greenfield, WI 53220</address>
  </div>

  <!-- Right panel (cover) -->
  <div class="panel panel--right">
    <div class="brand-mark" style="top:326px;left:32px">
      <span class="brand-mark__dot" style="width:36px;height:36px"></span>
      <span style="font:700 13px/16px var(--serif);color:var(--ink)">Bay &amp; Meadow<br>Property Services</span>
    </div>
    <h1 class="cover-headline">WHERE EXPERTISE</h1>
    <p class="cover-sub">MEETS EXCEPTIONAL RETURNS</p>
    <p class="cover-intro">At Bay &amp; Meadow Property Services, we are your trusted partner in unlocking the full potential of your real estate investments</p>
    <div class="phone-pill">(555) 214-3860</div>
  </div>
</section>

<!-- ============ INSIDE SPREAD ============ -->
<section class="spread spread--inside">
  <svg class="spread__art" viewBox="0 0 760 588" aria-hidden="true">
    <path d="M0 0H640C560 10 430 40 330 62C250 78 180 82 120 66C70 53 30 40 0 22Z" fill="#262526"/>
    <path d="M0 26C30 44 70 58 120 70C180 86 250 82 330 66C430 44 560 14 640 2H700C600 20 450 54 340 80C250 100 170 104 110 90C60 78 25 62 0 44Z" fill="#0aa2c9"/>
    <path d="M560 0H620C680 4 730 20 760 36V58C730 40 690 22 640 10C610 4 585 2 560 0Z" fill="#0aa2c9"/>
    <path d="M0 562C25 574 50 584 75 588H0Z" fill="#0aa2c9"/>
    <path d="M300 588C420 560 540 530 640 524C700 521 740 532 760 542V588Z" fill="#0aa2c9"/>
    <path d="M260 588C400 568 520 548 620 546C680 545 730 552 760 562V566C720 556 660 552 600 554C500 558 400 574 300 588Z" fill="#ffffff"/>
    <path d="M560 588C640 560 710 552 760 566V588Z" fill="#262526"/>
  </svg>
  <div class="fold" style="left:253px"></div>
  <div class="fold" style="left:507px"></div>

  <!-- Left panel: about -->
  <div class="panel panel--left">
    <p class="about-kicker">ABOUT</p>
    <h2 class="about-title">BAY &amp; MEADOW<br>PROPERTY SERVICES</h2>
    <div class="rule" style="top:144px"></div>
    <h3 class="about-lead">GROUNDED IN EXPERTISE.<br>BUILT FOR PERFORMANCE.</h3>
    <p class="copy" style="top:183px">At Bay &amp; Meadow Property Services, we combine boots-on-the-ground experience with next-level strategy to unlock value in every square foot. Whether it’s transforming a vacant lot into a high-performing storage facility or managing a multi-unit StayNest portfolio remotely, we specialize in making real estate work smarter—for you.</p>
    <p class="copy" style="top:289px">We are operators, builders, and investors who understand the intricacies of today’s most lucrative real estate verticals: Short-Term Rentals (STRs), Residential Rentals, and Mini/Maxi Storage Facilities. We don’t just offer services—we deliver outcomes that scale wealth, reduce risk, and free up your time.</p>
    <div class="rule" style="top:395px"></div>
    <h3 class="approach-title">OUR APPROACH</h3>
    <p class="copy" style="top:417px">We provide fully integrated real estate solutions—from sourcing and design through stabilization and exit. Our team thrives at the intersection of strategy and execution, blending in-the-field construction know-how with automated management systems and financial insight.</p>
    <p class="copy" style="top:510px">Whether you’re an investor looking to go hands-off or a hands-on owner needing expert strategy, we tailor our approach to fit your lifestyle, capital goals, and timeline.</p>
  </div>

  <!-- Middle panel: expertise -->
  <div class="panel panel--middle">
    <div class="section-pill" style="top:61px;left:21px;width:203px">OUR EXPERTISE INCLUDES</div>

    <svg class="expertise-icon" style="top:104px" viewBox="0 0 28 28" aria-hidden="true"><path d="M9 10v6M13 7v9M17 9v7M21 4v12" stroke="#0aa2c9" stroke-width="2.4"/><path d="M7 8l5-4 4 3 6-5" stroke="#0aa2c9" stroke-width="1.4" fill="none"/><path d="M1 22c4-3 8-4 12-2h8c1 0 1 2 0 2h-6M1 26l5-1c4 0 8 1 12-1l8-5" stroke="#0aa2c9" stroke-width="2" fill="none"/></svg>
    <h3 class="expertise-head" style="top:107px">INVESTMENT &amp; OPPORTUNITY<br>EVALUATION:</h3>
    <p class="expertise-copy" style="top:143px">Finding and analyzing lucrative real estate projects tailored to your goals.</p>

    <svg class="expertise-icon" style="top:183px" viewBox="0 0 28 28" aria-hidden="true"><path d="M3 23L23 3l3 3L6 26z" fill="none" stroke="#0aa2c9" stroke-width="2"/><path d="M8 19l2 2M11 16l2 2M14 13l2 2M17 10l2 2" stroke="#0aa2c9" stroke-width="1.4"/><path d="M4 4l18 18-1 4-4-1L3 7z" fill="#0aa2c9"/></svg>
    <h3 class="expertise-head" style="top:184px">DESIGN &amp; PROJECT<br>MANAGEMENT:</h3>
    <p class="expertise-copy" style="top:218px">Overseeing new construction or refurbishment projects to enhance property value.</p>

    <svg class="expertise-icon" style="top:268px" viewBox="0 0 28 28" aria-hidden="true"><rect x="3" y="4" width="17" height="22" rx="2" fill="none" stroke="#0aa2c9" stroke-width="2"/><rect x="8" y="2" width="7" height="4" fill="#0aa2c9"/><path d="M7 11h3M7 16h3M7 21h3" stroke="#0aa2c9" stroke-width="2"/><circle cx="20" cy="19" r="6" fill="#0aa2c9"/><path d="M17 19l2 2 4-4" stroke="#fff" stroke-width="1.8" fill="none"/></svg>
    <h3 class="expertise-head" style="top:272px">COMPLIANCE &amp;<br>OPERATIONALIZATION:</h3>
    <p class="expertise-copy" style="top:308px">Navigating local regulations and preparing properties for occupancy with minimal vacancies.</p>

    <svg class="expertise-icon" style="top:344px" viewBox="0 0 28 28" aria-hidden="true"><path d="M2 13L14 2l12 11" stroke="#0aa2c9" stroke-width="2.4" fill="none"/><path d="M5 12v14h18V12" stroke="#0aa2c9" stroke-width="2.2" fill="none"/><circle cx="14" cy="15" r="3" fill="#0aa2c9"/><path d="M8 26c0-4 3-6 6-6s6 2 6 6z" fill="#0aa2c9"/></svg>
    <h3 class="expertise-head" style="top:348px">TENANT &amp; PROPERTY<br>MANAGEMENT:</h3>
    <p class="expertise-copy" style="top:384px">Providing seamless day-to-day management for tenants and properties to ensure optimal satisfaction and financial performance</p>

    <svg class="expertise-icon" style="top:437px" viewBox="0 0 28 28" aria-hidden="true"><path d="M10 6V2h16v24H10v-4" stroke="#0aa2c9" stroke-width="2" fill="none"/><path d="M16 3l10-1v24l-10-2z" fill="#0aa2c9"/><path d="M1 14h12M9 10l4 4-4 4" stroke="#0aa2c9" stroke-width="2" fill="none"/></svg>
    <h3 class="expertise-head" style="top:445px">STRATEGIC EXITS:</h3>
    <p class="expertise-copy" style="top:473px">Guiding you through the sale process to secure top dollar for your investments.</p>
  </div>

  <!-- Right panel: sectors -->
  <div class="panel panel--right">
    <div class="tab" style="top:30px;width:203px;padding-left:24px;height:27px">SECTORS WE SERVICE</div>

    <svg class="sector-icon" style="top:67px" viewBox="0 0 40 30" aria-hidden="true"><path d="M20 2L8 12v16h24V12z" fill="#0aa2c9"/><path d="M4 16l8-7M36 16l-8-7" stroke="#0aa2c9" stroke-width="3"/><rect x="2" y="16" width="8" height="12" fill="#0aa2c9"/><rect x="30" y="16" width="8" height="12" fill="#0aa2c9"/><rect x="17" y="18" width="6" height="10" fill="#fff"/><rect x="11" y="14" width="4" height="4" fill="#fff"/><rect x="25" y="14" width="4" height="4" fill="#fff"/></svg>
    <p class="sector-label" style="top:106px">RESIDENTIAL REAL ESTATE SECTOR</p>

    <svg class="sector-icon" style="top:133px" viewBox="0 0 40 30" aria-hidden="true"><rect x="6" y="2" width="28" height="10" rx="2" fill="#0aa2c9"/><rect x="9" y="5" width="9" height="5" rx="1" fill="#fff"/><rect x="22" y="5" width="9" height="5" rx="1" fill="#fff"/><rect x="4" y="13" width="32" height="9" fill="#0aa2c9"/><rect x="4" y="22" width="4" height="6" fill="#0aa2c9"/><rect x="32" y="22" width="4" height="6" fill="#0aa2c9"/></svg>
    <p class="sector-label" style="top:174px">SHORT-TERM REAL ESTATE SECTOR</p>

    <svg class="sector-icon" style="top:207px" viewBox="0 0 40 30" aria-hidden="true"><path d="M6 6h28v24H6z" fill="#0aa2c9"/><rect x="9" y="3" width="22" height="3" fill="#0aa2c9"/><path d="M10 11h20M10 15h20M10 19h20M10 23h20M10 27h20" stroke="#fff" stroke-width="1.6"/></svg>
    <p class="sector-label" style="top:247px">MINI &amp; MAXI STORAGE SECTOR</p>

    <div class="services-banner">SERVICES WE OFFER IN<br>EACH SECTOR</div>

    <svg class="sector-icon" style="top:309px;height:36px" viewBox="0 0 40 36" aria-hidden="true"><circle cx="24" cy="9" r="7" fill="#0aa2c9"/><circle cx="24" cy="9" r="2.5" fill="#fff"/><path d="M22 15l-8 16 3 2 1-3 3 1 1-3-2-1 5-10z" fill="#0aa2c9"/><circle cx="15" cy="11" r="5" fill="none" stroke="#0aa2c9" stroke-width="2.4"/><path d="M14 16v14l3 2" stroke="#0aa2c9" stroke-width="2.4" fill="none"/></svg>
    <p class="sector-label" style="top:354px">RESIDENTIAL REAL ESTATE SERVICE</p>

    <svg class="sector-icon" style="top:382px" viewBox="0 0 40 30" aria-hidden="true"><path d="M20 1L4 14h4v15h24V14h4z" fill="#0aa2c9"/><rect x="13" y="13" width="14" height="13" rx="1" fill="#fff"/><path d="M15 15h10v3H15z" fill="#0aa2c9"/><path d="M15 20h2v2h-2zM19 20h2v2h-2zM23 20h2v2h-2zM15 23h2v2h-2zM19 23h2v2h-2zM23 23h2v2h-2z" fill="#0aa2c9"/></svg>
    <p class="sector-label" style="top:424px">SHORT-TERM REAL ESTATE SERVICE</p>

    <svg class="sector-icon" style="top:450px" viewBox="0 0 40 30" aria-hidden="true"><path d="M20 1L3 10v3h34v-3z" fill="#0aa2c9"/><path d="M6 13v16h28V13" fill="none" stroke="#0aa2c9" stroke-width="3"/><rect x="10" y="18" width="6" height="5" fill="#0aa2c9"/><rect x="17" y="18" width="6" height="5" fill="#0aa2c9"/><rect x="24" y="18" width="6" height="5" fill="#0aa2c9"/><rect x="10" y="24" width="6" height="5" fill="#0aa2c9"/><rect x="17" y="24" width="6" height="5" fill="#0aa2c9"/><rect x="24" y="24" width="6" height="5" fill="#0aa2c9"/></svg>
    <p class="sector-label" style="top:491px">STORAGE FACILITY SERVICES</p>
  </div>
</section>

</body>
</html>
```